Corporate Design für Malermeister
Super Arbeit von dem ersten Entwurf an. Schnelle und präzise Umstzung von Änderungen. Durch tolle Vorschläge des Designers sowie meiner Vorstellung ist ein für mich perfektes und stimmiges Corparate Design entstanden. Die Zusammenarbeit war rundum ein voller Erfolg! Sehr zu empfehlen! Auch hier noch mal Danke für deine präzise und schnelle Arbeit. Mann merkt, dass hier mit einem Profi gearbeitet wird!
Zielgruppe
Ich bin Malermeister ,
wir bieten komplettrenovierungen an vom Gestalten der Oberflächen, kreative Wandgestaltung Trockenbau, Bodenverlegearbeiten Parkett, Laminat, Teppich, designböden etc.
Fokus liegt bei den Malerarbeiten! Auch Fassaden werden restaurariert und gestaltet
Wir wollen modern und hochwertig rüber kommen
Aufgabenstellung
Das Logo soll zeigen, dass wir ein moderner kreativer Betrieb sind
da wir eine Diesntaleistung anbieten sollte es auch auf Vertrauen asutrahlen

```html
<!DOCTYPE html>
<html lang="de">
<head>
<meta charset="utf-8">
<title>Briefpapier Farbraum – Entwurf 03</title>
<link href="https://fonts.googleapis.com/css2?family=PT+Sans:wght@400;700&display=swap" rel="stylesheet">
<style>
:root{
  --frame:#0f70b7;
  --brand:#0f6db5;
  --ink:#1a1a1a;
  --grey:#555;
  --caption:#9a9a9a;
  --paper:#fff;
  --wash:#ececec;
}
*{margin:0;padding:0;box-sizing:border-box}
html,body{width:1200px;height:2400px;overflow:hidden;background:var(--frame)}
body{font-family:"PT Sans",sans-serif;color:var(--ink);position:relative}
.board{position:absolute;left:15px;top:30px;width:1170px;height:2340px;background:var(--paper)}
.caption{position:absolute;left:0;top:138px;width:1200px;text-align:center;color:var(--caption);font-size:19px;line-height:24px}
.sheet{position:absolute;left:241px;width:718px;height:1016px;background:var(--paper);box-shadow:0 0 8px rgba(0,0,0,.28);overflow:hidden}
.sheet--first{top:269px;height:1013px}
.sheet--follow{top:1326px}
.brand{position:absolute;left:491px;top:116px}
.brand__name{display:flex;align-items:center;gap:8px;font-weight:700;font-size:34px;line-height:38px;color:var(--brand)}
.brand__mark{width:12px;height:12px;background:var(--brand);flex:none}
.brand__trade{font-size:14px;color:var(--grey);margin-top:2px}
.brand__claim{font-size:12.5px;color:var(--grey);margin-top:1px}
.fold-mark{position:absolute;left:0;top:353px;width:21px;height:1px;background:#777}
.sender-line{position:absolute;left:82px;top:176px;font-size:8px;color:#333}
.recipient{position:absolute;left:82px;top:206px;font-size:13px;line-height:17px}
.contact{position:absolute;left:492px;top:201px;font-size:10.5px;line-height:15px}
.contact__person{margin-left:17px;color:var(--brand);font-weight:700;font-size:12px;line-height:14px}
.contact__role{margin-left:17px;font-size:10.5px;line-height:12px;color:#333}
.contact__row{display:flex;align-items:center;gap:5px;color:#333}
.contact__row svg{width:12px;height:12px;fill:var(--brand);flex:none}
.contact__row--web{color:var(--brand);font-weight:700}
.gap{height:11px}
.date{position:absolute;left:482px;top:360px;font-size:13px}
.letter{position:absolute;left:80px;top:420px;width:580px;font-size:13px;line-height:17px}
.letter p{margin-bottom:17px}
.signature{display:block;width:118px;height:24px;background:#d6d6d6;border-radius:3px;margin:-4px 0 8px}
.backdrop{position:absolute;left:30px;width:620px;height:330px;border-radius:60px;background:radial-gradient(ellipse at center,rgba(236,236,236,.9) 0%,rgba(236,236,236,.35) 60%,rgba(236,236,236,0) 100%)}
.sheet--first .backdrop{top:505px}
.sheet--follow .backdrop{top:462px}
.letter,.recipient{z-index:1}
.footer{position:absolute;left:0;top:910px;width:100%;height:110px}
.footer__col{position:absolute;top:0;height:110px;border-left:2.5px solid var(--brand);padding-left:5px;font-size:9.5px;line-height:12.7px;color:#333}
.footer__col .blank{height:12.7px}
.footer__col a{color:var(--brand);text-decoration:none}
.footer__col--company{left:48px}
.footer__col--contact{left:249px}
.footer__col--bank{left:456px}
</style>
</head>
<body>
<div class="board"></div>
<div class="caption">
  Briefpapier &nbsp;Farbraum - Entwurf 03 &nbsp;|&nbsp; Seite 1 + 2<br>
  Standard 210 x 297 mm &nbsp;|&nbsp; hochkant<br>
  jeweils einseitig 4 c &nbsp;|&nbsp; umlaufender Beschnitt 1 mm
</div>

<section class="sheet sheet--first">
  <div class="backdrop" role="img" aria-label="Große, blasse Pinselstrich-Fläche im Hintergrund"></div>
  <div class="brand">
    <div class="brand__name"><span class="brand__mark"></span>Farbraum</div>
    <div class="brand__trade">Malermeisterbetrieb</div>
    <div class="brand__claim">Sorgfalt in jeder Schicht</div>
  </div>
  <div class="sender-line">Farbraum &nbsp;| &nbsp;Lindenallee 14 &nbsp;| &nbsp;48301 Hellbrück</div>
  <div class="recipient">Lena Beispiel<br>Musterstraße 7<br>24536 Musterstadt</div>
  <div class="contact">
    <div class="contact__person">Jonas Feldkamp</div>
    <div class="contact__role">Malermeister</div>
    <div class="gap"></div>
    <div class="contact__row"><svg viewBox="0 0 12 12"><path d="M6 1 0.5 6h1.8v5h2.9V8h1.6v3h2.9V6h1.8z"/></svg><span>Lindenallee 14</span></div>
    <div class="contact__row"><span style="margin-left:17px">48301 Hellbrück</span></div>
    <div class="gap"></div>
    <div class="contact__row"><svg viewBox="0 0 12 12"><path d="M3.5 0.5h5a1 1 0 0 1 1 1v9a1 1 0 0 1-1 1h-5a1 1 0 0 1-1-1v-9a1 1 0 0 1 1-1zm.5 1.5v7h4V2z"/></svg><span>0170 - 482 17 39</span></div>
    <div class="contact__row"><svg viewBox="0 0 12 12"><path d="M0.5 2.5h11v7h-11zM1 3l5 3.5L11 3"/></svg><span>maler@farbraum-betrieb.de</span></div>
    <div class="contact__row contact__row--web"><svg viewBox="0 0 12 12"><circle cx="6" cy="6" r="5.5"/></svg><span>www.farbraum-betrieb.de</span></div>
  </div>
  <div class="fold-mark"></div>
  <div class="date">Musterdorf, 07. Januar 2018</div>
  <div class="letter">
    <p>Sehr geehrter Herr Musterschüler,</p>
    <p>Eine wunderbare Heiterkeit hat meine ganze Seele eingenommen, gleich den süßen Frühlingsmorgen, die ich mit ganzem Herzen genieße. Ich bin allein und freue mich meines Lebens in dieser Gegend, die für solche Seelen geschaffen ist wie die meine. Ich bin so glücklich, mein Bester, so ganz in dem Gefühle von ruhigem Dasein versunken, daß meine Kunst darunter leidet. Ich könnte jetzt nicht zeichnen, nicht einen Strich, und bin nie ein größerer Maler gewesen als in diesen Augenblicken.</p>
    <p>Wenn das liebe Tal um mich dampft, und die hohe Sonne an der Oberfläche der undurchdringlichen Finsternis meines Waldes ruht, und nur einzelne Strahlen sich in das innere Heiligtum stehlen, ich dann im hohen Grase am fallenden Bache liege, und näher an der Erde tausend mannigfaltige Gräschen mir merkwürdig werden; wenn ich das Wimmeln der kleinen Welt zwischen Halmen, die unzähligen, unergründlichen Gestalten der Würmchen, der Mückchen näher an meinem Herzen fühle, und fühle die Gegenwart des Allmächtigen, der uns nach seinem Bilde schuf, das Wehen des Allliebenden, der uns in ewiger Wonne schwebend trägt und erhält; mein Freund! Wenn's dann um meine Augen dämmert, und die Welt um mich her und der Himmel ganz in meiner Seele ruhn wie die Gestalt einer</p>
    <p>Mit freundlichen Grüßen</p>
    <span class="signature" role="img" aria-label="Handschriftliche Unterschrift"></span>
    <div>Jonas Feldkamp</div>
  </div>
  <footer class="footer">
    <div class="footer__col footer__col--company">Farbraum<div class="blank"></div>Jonas Feldkamp<br>Lindenallee 14<br>48301 Hellbrück</div>
    <div class="footer__col footer__col--contact">Kontakt:<div class="blank"></div>0170 - 482 17 39<br>maler@farbraum-betrieb.de<br><a>www.farbraum-betrieb.de</a></div>
    <div class="footer__col footer__col--bank">Kreisbank Talgrund<br>IBAN: DE 00 1200 3400 5600 7800 90<br>BIC: TALGDE21XXX<br>Finanzamt Hellbrück<br>Steuernummer: 40120385716</div>
  </footer>
</section>

<section class="sheet sheet--follow">
  <div class="backdrop" role="img" aria-label="Große, blasse Pinselstrich-Fläche im Hintergrund"></div>
  <div class="brand">
    <div class="brand__name"><span class="brand__mark"></span>Farbraum</div>
    <div class="brand__trade">Malermeisterbetrieb</div>
    <div class="brand__claim">Sorgfalt in jeder Schicht</div>
  </div>
  <div class="fold-mark"></div>
  <footer class="footer">
    <div class="footer__col footer__col--company">Farbraum<div class="blank"></div>Jonas Feldkamp<br>Lindenallee 14<br>48301 Hellbrück</div>
    <div class="footer__col footer__col--contact">Kontakt:<div class="blank"></div>0170 - 482 17 39<br>maler@farbraum-betrieb.de<br><a>www.farbraum-betrieb.de</a></div>
    <div class="footer__col footer__col--bank">Kreisbank Talgrund<br>IBAN: DE 00 1200 3400 5600 7800 90<br>BIC: TALGDE21XXX<br>Finanzamt Hellbrück<br>Steuernummer: 40120385716</div>
  </footer>
</section>
</body>
</html>
```